Chocolate covered bananas

“I am starting a new venture making chocolate coated frozen bananas. At start up I intend to have 4 different types:
3 will be single bananas ( Dark Chocolate, Dark chocolate with sprinkles and Dark Chocolate & Almonds) sold in individual packets, 70MM(W) x 215mm(L)

The other will be Banana Pops (smaller pieces of banana) sold in a 500g bag and then packed in a 165mm(L) x 50mm(W) X 165mm(H) cardboard box

The packaging will need my logo the wording “Chocolate Coated Frozen Banana” and the slogan “Sweet Bite Delight” on it. A picture of a Banana and Chocolate (The chocolate can be on the banana, getting poured on it, or even beside it).
I would like the words “Zero Trans-fat” on both the packaging (3 variations) and the 500g container along with “Healthy Dessert Treat” on the Container.

I need the Ingredients and nutritional information on the back"

one version can be submitted within the Contest period, however the winner is required to provide all 4 versions as part of the project.

Good Luck
Updates

JUST A QUICK NOTE THE BANANAS WILL BE ON A ICE-CREAM STICK AND THE BANANA POPS WILL BE ON A POPSICLE STICK.

Here are a couple of examples from places in America (no competition to me I am in another country) I'm am looking for something similar in size. as the packets in wholly mangoes and the cartons in gretas melons. http://www.wholly-mangoes.net/products.php and http://www.gretasmelons.com/our-products/ I hope this helps Regards Colin.

Hi I am getting some great designs Most are dark brown (or chocolate ) in colour they look good however most ice cream packs are dark and I think in order for these to stand out they need to be brighter with the chocolate as a secondary colour. Regards Colin.

Hi all great designs it will be very hard to pick. just a quick note I made a spelling mistake in my brief it is HEALTHY DESSERT TREAT (NOT DESERT) SORRY Regards Colin.

I would like to thank everyone for there time and effort they have put in to my packaging design contest. I am meeting with the packaging company on Thursday and will have a decision Thursday night. Regards Colin.

Target Market(s)

I plan to go down the track that these are a healthy tasty fun treat.
I will be using real Bananas and Real chocolate.

```html
<!DOCTYPE html>
<html lang="en">
<head>
<meta charset="utf-8">
<title>Sunny Split – Chocolate Coated Frozen Banana Pack</title>
<link rel="stylesheet" href="https://fonts.googleapis.com/css2?family=Titan+One&family=Delius+Swash+Caps&display=swap">
<style>
  :root {
    --canvas: #ffffff;
    --sun-yellow: #fdd80f;
    --pale-yellow: #fff27a;
    --deep-orange: #e07a30;
    --choc-dark: #2a1408;
    --choc-mid: #5a2e12;
    --slogan-red: #7a1d0c;
    --lime: #c8f000;
    --lime-band: #9be20a;
    --ink: #111111;
  }
  html, body {
    margin: 0;
    padding: 0;
    width: 1200px;
    height: 1000px;
    overflow: hidden;
    background: var(--canvas);
  }
  .canvas {
    position: relative;
    width: 1200px;
    height: 1000px;
  }
  .pack {
    position: absolute;
    left: 481px;
    top: 68px;
    width: 283px;
    height: 869px;
  }
  .brand-name {
    font-family: "Titan One", sans-serif;
    font-size: 15px;
    fill: var(--sun-yellow);
  }
  .slogan {
    font-family: "Delius Swash Caps", cursive;
    font-size: 17px;
    fill: var(--slogan-red);
  }
  .headline {
    font-family: "Titan One", sans-serif;
    stroke: var(--ink);
    stroke-linejoin: round;
    paint-order: stroke fill;
  }
  .headline--chocolate { font-size: 36px; stroke-width: 7px; fill: url(#chocText); }
  .headline--coated { font-size: 34px; stroke-width: 7px; fill: url(#coatText); }
  .headline--frozen { font-size: 25px; stroke-width: 6px; fill: var(--sun-yellow); }
  .badge-text {
    font-family: "Titan One", sans-serif;
    font-size: 14px;
    fill: var(--ink);
    letter-spacing: 0.5px;
  }
</style>
</head>
<body>
<div class="canvas">
  <svg class="pack" viewBox="0 0 283 869" xmlns="http://www.w3.org/2000/svg">
    <defs>
      <linearGradient id="packBg" x1="0" y1="0" x2="0" y2="1">
        <stop offset="0" stop-color="var(--sun-yellow)"/>
        <stop offset="0.35" stop-color="var(--pale-yellow)"/>
        <stop offset="0.6" stop-color="#f7c070"/>
        <stop offset="0.8" stop-color="var(--deep-orange)"/>
        <stop offset="1" stop-color="#b65a22"/>
      </linearGradient>
      <radialGradient id="glow" cx="0.5" cy="0.5" r="0.5">
        <stop offset="0" stop-color="#fff8e0" stop-opacity="0.9"/>
        <stop offset="1" stop-color="#fff8e0" stop-opacity="0"/>
      </radialGradient>
      <linearGradient id="chocText" x1="0" y1="0" x2="0" y2="1">
        <stop offset="0" stop-color="#d9a46a"/>
        <stop offset="0.5" stop-color="#8a4a1c"/>
        <stop offset="1" stop-color="#5a2a0c"/>
      </linearGradient>
      <linearGradient id="coatText" x1="0" y1="0" x2="0" y2="1">
        <stop offset="0" stop-color="#f3e4cc"/>
        <stop offset="0.5" stop-color="#b88a5a"/>
        <stop offset="1" stop-color="#6b3e1a"/>
      </linearGradient>
      <linearGradient id="bananaFill" x1="0" y1="0" x2="1" y2="0">
        <stop offset="0" stop-color="var(--choc-dark)"/>
        <stop offset="0.6" stop-color="var(--choc-mid)"/>
        <stop offset="1" stop-color="var(--choc-dark)"/>
      </linearGradient>
      <linearGradient id="splashFill" x1="0" y1="0" x2="0" y2="1">
        <stop offset="0" stop-color="var(--choc-mid)"/>
        <stop offset="1" stop-color="var(--choc-dark)"/>
      </linearGradient>
    </defs>

    <rect class="pack-bg" width="283" height="869" fill="url(#packBg)"/>
    <ellipse class="pack-glow" cx="130" cy="470" rx="140" ry="190" fill="url(#glow)"/>

    <g class="brand">
      <circle cx="144" cy="110" r="62" fill="var(--choc-dark)"/>
      <text class="brand-name" x="144" y="115" text-anchor="middle">Sunny Split</text>
    </g>

    <text class="slogan" x="144" y="192" text-anchor="middle">Sweet Bite Delight</text>

    <g class="product-name">
      <text class="headline headline--chocolate" x="140" y="290" text-anchor="middle" transform="rotate(-18 140 290)">Chocolate</text>
      <text class="headline headline--coated" x="128" y="330" text-anchor="middle" transform="rotate(-18 128 330)">Coated</text>
      <text class="headline headline--frozen" x="150" y="383" text-anchor="middle" transform="rotate(-22 150 383)">Frozen Banana</text>
    </g>

    <rect class="product-photo" x="80" y="440" width="170" height="320" rx="60"
          fill="url(#bananaFill)" transform="rotate(-10 165 600)"
          role="img" aria-label="Chocolate coated frozen banana on an ice-cream stick"/>
    <rect class="chocolate-splash" x="0" y="745" width="283" height="50"
          fill="url(#splashFill)" opacity="0.85"
          role="img" aria-label="Splash of melted chocolate"/>

    <rect class="base-dark" x="0" y="790" width="283" height="79" fill="var(--choc-dark)"/>
    <rect class="base-band" x="0" y="790" width="283" height="17" fill="var(--lime-band)"/>
    <g class="claim-badge">
      <ellipse cx="144" cy="800" rx="58" ry="28" fill="var(--lime)" stroke="var(--choc-dark)" stroke-width="2"/>
      <text class="badge-text" x="144" y="797" text-anchor="middle">ZERO</text>
      <text class="badge-text" x="144" y="815" text-anchor="middle">TRANS-FAT</text>
    </g>
  </svg>
</div>
</body>
</html>
```